Corvane Electrical Solutions

On one side. LOGO (underneath:) Commercial Industrial Residential

- NAME & CONTACT DETAILS

Marcus T. Hollings
Project Manager

(Cell icon) (441) 582-6197
(Email icon) cvnelectricalsoultions@mailventra.com
(Facebook & Instagram icons )@cvnelectricalsolutions

Other side: LOGO - underneath ELECTRICAL CONSTRUCTION & MAINTENANCE . LED LIGHTING & AUTOMATION . LIFE SAFETY SYSTEMS (FIRE ALARM / SECURITY) . DATA & COMMUNICATION

```html
<!DOCTYPE html>
<html lang="en">
<head>
<meta charset="utf-8">
<title>Corvane Electrical Solutions – Business Card</title>
<link href="https://fonts.googleapis.com/css2?family=Lato:wght@400;700&display=swap" rel="stylesheet">
<style>
  :root {
    --stage: #1c1c1e;
    --card: #ffffff;
    --brand-teal: #1e5a6e;
    --ink-grey: #4a4a4a;
    --rule-grey: #c9c9c9;
  }
  * { box-sizing: border-box; margin: 0; padding: 0; }
  html, body {
    width: 1200px; height: 900px; overflow: hidden;
    background: var(--stage);
    font-family: "Lato", Arial, sans-serif;
  }
  .stage { position: relative; width: 1200px; height: 900px; }
  .card {
    position: absolute;
    width: 580px; height: 330px;
    background: var(--card);
    box-shadow: 0 18px 40px rgba(0,0,0,.55);
  }
  /* Services side */
  .card--services { left: 90px; top: 70px; }
  .card--services .brand {
    position: absolute; left: 0; right: 0; top: 78px;
    text-align: center;
  }
  .brand-name {
    color: var(--brand-teal);
    font-weight: 700;
    font-size: 26px;
    letter-spacing: 2px;
    text-transform: uppercase;
    display: inline-flex; align-items: center; gap: 12px;
  }
  .brand-mark { width: 16px; height: 16px; background: var(--brand-teal); display: inline-block; }
  .sectors {
    margin-top: 12px;
    color: var(--ink-grey);
    font-size: 14px;
    letter-spacing: .6px;
    text-transform: uppercase;
  }
  .services {
    position: absolute; left: 0; right: 0; top: 200px;
    text-align: center; list-style: none;
    color: var(--ink-grey);
    font-size: 14px; line-height: 1.35;
    letter-spacing: .4px; text-transform: uppercase;
  }
  /* Contact side */
  .card--contact { left: 530px; top: 500px; }
  .card--contact .brand {
    position: absolute; left: 28px; top: 140px; width: 220px;
  }
  .card--contact .brand-name { font-size: 19px; letter-spacing: 1.2px; line-height: 1.25; display: block; }
  .divider {
    position: absolute; left: 262px; top: 62px;
    width: 1px; height: 206px; background: var(--rule-grey);
  }
  .contact { position: absolute; left: 284px; top: 62px; }
  .person-name {
    color: var(--brand-teal); font-weight: 700;
    font-size: 20px; letter-spacing: .5px; text-transform: uppercase;
  }
  .person-role { color: var(--ink-grey); font-size: 14px; margin-top: 2px; }
  .contact-list { list-style: none; margin-top: 14px; }
  .contact-item {
    display: flex; align-items: center; gap: 9px;
    color: var(--ink-grey); font-size: 14px; height: 30px;
  }
  .contact-icon {
    width: 22px; height: 22px; flex: none;
    border: 1.5px solid var(--brand-teal); border-radius: 50%;
    display: flex; align-items: center; justify-content: center;
  }
  .contact-icon svg { width: 12px; height: 12px; }
  .contact-icon--plain::after {
    content: ""; width: 8px; height: 8px; border-radius: 50%;
    background: var(--brand-teal);
  }
</style>
</head>
<body>
<main class="stage">
  <section class="card card--services" aria-label="Card front: services">
    <div class="brand">
      <div class="brand-name"><span class="brand-mark"></span>Corvane Electrical Solutions</div>
      <p class="sectors">Commercial Industrial Residential</p>
    </div>
    <ul class="services">
      <li>Electrical Construction &amp; Maintenance</li>
      <li>LED Lighting &amp; Automation | Data &amp; Communication</li>
      <li>Life Safety Systems (Fire Alarm / Security)</li>
    </ul>
  </section>

  <section class="card card--contact" aria-label="Card back: contact details">
    <div class="brand"><span class="brand-name">Corvane Electrical Solutions</span></div>
    <div class="divider"></div>
    <div class="contact">
      <h1 class="person-name">Marcus T. Hollings</h1>
      <p class="person-role">Project Manager</p>
      <ul class="contact-list">
        <li class="contact-item">
          <span class="contact-icon">
            <svg viewBox="0 0 12 12"><rect x="3" y="1" width="6" height="10" rx="1" fill="none" stroke="#1e5a6e" stroke-width="1.3"/><line x1="5" y1="9.2" x2="7" y2="9.2" stroke="#1e5a6e" stroke-width="1"/></svg>
          </span>
          (441) 582-6197
        </li>
        <li class="contact-item">
          <span class="contact-icon">
            <svg viewBox="0 0 12 12"><rect x="1" y="3" width="10" height="7" fill="none" stroke="#1e5a6e" stroke-width="1.3"/><polyline points="1,3 6,7 11,3" fill="none" stroke="#1e5a6e" stroke-width="1.2"/></svg>
          </span>
          cvnelectricalsoultions@mailventra.com
        </li>
        <li class="contact-item"><span class="contact-icon contact-icon--plain"></span>@cvnelectricalsolutions</li>
        <li class="contact-item"><span class="contact-icon contact-icon--plain"></span>@cvnelectricalsolutions</li>
      </ul>
    </div>
  </section>
</main>
</body>
</html>
```